A new presentation to our clients

we are a Real Estate agency, our website is www.lirotama.com and it’s time to have a new, fashion and remarcable Business Card. we want to differentiate ourselves from other companies so we want a business card that differentiates us. we want the business card to impact our customers. in the competitive market that we have today, we have to be different and it is this difference that we seek

Target Market(s)

Real Estate Clients

Contact Information for Business Card

We search a totaly diferent card from the usual

Font styles to use
Sans Serif

Colors
e34197

Requirements
Must have
• Logo, adress, phone contact, e-mail, photo, and our website
Nice to have
• We would like to see a modern business card
Should not have
• Houses or building draws

```html
<!DOCTYPE html>
<html lang="en">
<head>
<meta charset="utf-8">
<title>Lirotama Business Card</title>
<link rel="stylesheet" href="https://fonts.googleapis.com/css2?family=Open+Sans:wght@400;600&family=Roboto:wght@700&display=swap">
<style>
  :root {
    --backdrop: #8a5a34;
    --kraft-light: #d9b486;
    --kraft-mid: #c89a68;
    --kraft-dark: #b98a58;
    --ink: #111111;
  }
  * { margin: 0; padding: 0; box-sizing: border-box; }
  html, body { width: 1200px; height: 900px; overflow: hidden; }
  body {
    position: relative;
    background: var(--backdrop);
    font-family: "Open Sans", Arial, sans-serif;
    color: var(--ink);
  }
  .card {
    position: absolute;
    left: 330px;
    width: 556px;
    height: 344px;
    background: linear-gradient(160deg, var(--kraft-light) 0%, var(--kraft-mid) 45%, var(--kraft-dark) 100%);
  }
  .card--front { top: 90px; }
  .card--back { top: 469px; }
  .contact {
    position: absolute;
    left: 0; right: 0; top: 64px;
    text-align: center;
  }
  .contact__name {
    font-family: "Roboto", Arial, sans-serif;
    font-weight: 700;
    font-size: 19.5px;
    line-height: 22px;
    letter-spacing: 0.2px;
  }
  .contact__role { font-size: 15.5px; line-height: 20px; }
  .icon-row {
    display: flex;
    justify-content: center;
    align-items: center;
    gap: 7px;
    margin: 12px 0 4px;
  }
  .icon-row__rule { width: 46px; height: 1px; background: var(--ink); margin: 0 1px; }
  .icon-row svg { width: 20px; height: 19px; display: block; }
  .contact__line { font-size: 15.5px; line-height: 20px; }
  .contact__divider { width: 206px; height: 1px; background: var(--ink); margin: 8px auto 8px; }
  .brand {
    position: absolute;
    inset: 0;
    display: flex;
    justify-content: center;
    align-items: center;
    padding-bottom: 8px;
    font-family: "Open Sans", Arial, sans-serif;
    font-weight: 600;
    font-size: 50px;
    letter-spacing: 1px;
  }
</style>
</head>
<body>
  <section class="card card--front">
    <div class="contact">
      <p class="contact__name">DANIEL FERREIRA</p>
      <p class="contact__role">Managing Director</p>
      <div class="icon-row">
        <span class="icon-row__rule"></span>
        <svg viewBox="0 0 20 19" aria-label="Phone"><rect width="20" height="19" fill="#111"/><path d="M4 7c0-2 12-2 12 0v1h-3V7H7v1H4z M6 9h8l2 5H4z" fill="#c89a68"/></svg>
        <svg viewBox="0 0 20 19" aria-label="Fax"><rect width="20" height="19" fill="#111"/><path d="M6 3h8v4H6z M3 8h14v6h-3v2H6v-2H3z" fill="#c89a68"/><rect x="7" y="12" width="6" height="3" fill="#111"/></svg>
        <svg viewBox="0 0 20 19" aria-label="Email"><rect width="20" height="19" fill="#111"/><rect x="3" y="5" width="14" height="9" fill="#c89a68"/><path d="M3 5l7 5 7-5" stroke="#111" stroke-width="1.2" fill="none"/></svg>
        <svg viewBox="0 0 20 19" aria-label="Website"><rect width="20" height="19" fill="#111"/><circle cx="10" cy="9.5" r="6" fill="#c89a68"/><path d="M7 6c2 1 1 3 3 3s1 3 0 4M13 6c-1 1 0 2 1 2" stroke="#111" stroke-width="1.4" fill="none"/></svg>
        <span class="icon-row__rule"></span>
      </div>
      <p class="contact__line">(+351) 210 555 482</p>
      <p class="contact__line">(+351) 210 555 489</p>
      <p class="contact__line">geral@lirotama.com</p>
      <p class="contact__line">www.lirotama.com</p>
      <div class="contact__divider"></div>
      <p class="contact__line">Rua das Amoreiras, 117</p>
      <p class="contact__line">4100-052, Porto</p>
    </div>
  </section>
  <section class="card card--back">
    <p class="brand">Lirotama</p>
  </section>
</body>
</html>
```